MS Word Template needed for a company specialized in network and security infrastructures

We need a new MS Word Template. <br/>Our activity is services in IT (network infrastructure and security). We usually use french language. <br/>The template must be nice and beautiful, and easy to use. If possible, try to use as less as possible text zones to simplify redaction tasks. And try to use "native" polices in MS Word. I attached sample documents for example. Please try to use the same colour codes.

Target Market(s)

Consulting in Network and security domain

Industry/Entity Type

It Service

Colors

Designer to choose colors to be used in the design.

Requirements
Must have
• - Nice design
• - Easy to use
• - very professional aspect
Nice to have
• - actual oxa cable partners logo
• - actual colour code

```html
<!DOCTYPE html>
<html lang="en">
<head>
<meta charset="utf-8">
<title>Oxa Cable Partners – Word Template Pages</title>
<link href="https://fonts.googleapis.com/css2?family=Open+Sans:wght@400;600;700&family=Tinos&display=swap" rel="stylesheet">
<style>
:root{
  --bg:#8f8f8f;
  --teal:#2a9ea2;
  --teal-light:#c4e7ea;
  --navy:#1e3a55;
  --green:#7fc47a;
  --green-soft:#a9c98d;
  --grey-row:#d4d4d4;
  --dark-row:#3d3d3d;
  --text:#4a4a4a;
  --rule:#c9c9c9;
}
*{margin:0;padding:0;box-sizing:border-box}
html,body{width:890px;height:1200px;overflow:hidden;background:var(--bg)}
body{position:relative;font-family:"Open Sans",Arial,sans-serif;color:var(--text)}
.page{position:absolute;width:254px;height:360px;background:#fff;overflow:hidden;padding:24px 17px 0}
.dots{display:flex;gap:2px;margin-bottom:3px}
.dots i{width:3.5px;height:3.5px;border-radius:50%;background:var(--teal)}
.dots i:last-child{background:var(--navy)}
.title{font-family:"Tinos","Times New Roman",serif;font-size:11.5px;color:#222;text-transform:uppercase;letter-spacing:.2px;margin-bottom:10px}
.title span{color:var(--teal)}
.body{font-size:3.9px;line-height:1.55;margin-bottom:4px;color:var(--text)}
.body a,.hl{color:var(--teal);text-decoration:none}
.hl-red{color:#c0392b}
.sub{font-size:7px;color:#333;margin:6px 0 2px;font-weight:600}
.quote{font-size:5.2px;line-height:1.3;color:var(--green-soft);font-weight:600;margin-bottom:6px}
.photo{background:linear-gradient(160deg,#dfe6ec,#8ea3b6 55%,#3e5268);}
.decor{position:absolute;background:linear-gradient(200deg,#d7e6dc 0%,#e6ebef 40%,#d7e8ef 70%,#eef2f4 100%);opacity:.85}
.brand{display:flex;align-items:center;gap:4px;color:var(--teal);font-weight:600;text-transform:uppercase}
.brand i{border-radius:50%;background:var(--teal);display:block}
.footer{position:absolute;left:17px;right:17px;bottom:13px;display:flex;align-items:center;gap:5px}
.footer .brand{font-size:3.2px}
.footer .brand i{width:7px;height:7px}
.footer .line{flex:1;height:.6px;background:var(--rule)}
.footer .num{width:12px;height:6px;border-radius:3px;background:var(--navy);color:#fff;font-size:3.6px;display:flex;align-items:center;justify-content:center}
/* cover */
.cover .brand{position:absolute;top:20px;left:128px;font-size:7px}
.cover .brand i{width:24px;height:24px}
.cover-title{position:absolute;left:26px;top:276px;font-size:14px;line-height:1.45;font-weight:700;color:#222}
.cover-band{position:absolute;left:0;right:0;top:330px;height:17px;background:var(--teal);color:#fff;font-size:6px;font-weight:700;display:flex;align-items:center;justify-content:center}
/* toc */
.toc-head{font-size:7px;font-weight:600;color:#333;margin:4px 0 6px}
.toc li{list-style:none;display:flex;font-size:3.6px;line-height:2.2;color:#333}
.toc li .lead{flex:1;border-bottom:.5px dotted #777;margin:0 3px 1.8px}
.toc li.l2{padding-left:4px;color:#666}
.toc li.l3{padding-left:8px;color:#666}
.toc li.b{font-weight:700}
/* vision */
.band{display:flex;height:23px;margin-bottom:7px}
.band .icon{width:23px;background:var(--teal);display:flex;align-items:center;justify-content:center}
.band .txt{flex:1;background:var(--green);font-size:4.4px;line-height:1.3;color:#1f3b2a;padding:3px 8px 0 16px}
/* exec */
.h-num{font-size:6.4px;color:#333;margin:4px 0 4px}
.it{font-style:italic;font-size:3.9px;color:#777;margin-bottom:1px}
/* two column */
.cols{display:flex;gap:10px}
.cols .left{width:90px;flex:none}
.cols .right{flex:1}
/* tables */
table{width:100%;border-collapse:separate;border-spacing:0 1.2px;font-size:3.4px;margin:4px 0 6px}
th{background:var(--grey-row);font-weight:400;color:#333;padding:.8px 2px}
td{background:var(--teal-light);padding:.6px 4px;color:#333}
td+td{text-align:center;border-left:2px solid #fff}
tr.tot td{font-weight:700}
tr.grand td{background:var(--teal);color:#fff;font-weight:700}
table.dark th{background:var(--dark-row);color:#fff}
th+th{border-left:2px solid #fff}
/* back */
.back-foot{position:absolute;left:52px;top:322px;display:flex;align-items:center;gap:6px;font-size:3px;color:#444;line-height:1.55}
.back-foot .brand{font-size:4.2px}
.back-foot .brand i{width:10px;height:10px}
.back-foot .sep{width:.6px;height:18px;background:var(--teal)}
.back-foot .ic{display:inline-block;width:3px;height:3px;border-radius:50%;background:var(--teal);margin-right:2px;vertical-align:middle}
</style>
</head>
<body>

<!-- Cover -->
<section class="page cover" style="left:28px;top:28px">
  <div class="decor" role="img" aria-label="Soft pattern of pale green, blue and grey triangles" style="left:8px;top:55px;width:190px;height:255px;clip-path:polygon(35% 0,70% 10%,100% 45%,75% 100%,20% 100%,0 40%)"></div>
  <div class="brand"><i></i>Oxa Cable Partners</div>
  <h1 class="cover-title">LOREM IPSUM IS SIMPLY<br>DUMMY HAS BEEN</h1>
  <div class="cover-band">LOREM IPSUM IS SIMPLY ETIAM VESTIBULUM</div>
</section>

<!-- Table of contents -->
<section class="page" style="left:316px;top:28px">
  <div class="dots"><i></i><i></i><i></i></div>
  <h2 class="title">Table of <span>Contents</span></h2>
  <p class="toc-head">Contents</p>
  <ul class="toc">
    <li class="b">1. Table of Contents<span class="lead"></span>01</li>
    <li class="l2">1.1. Executive Summary<span class="lead"></span>02</li>
    <li class="l3">1.1.1. Our Understanding of Your Needs<span class="lead"></span>02</li>
    <li class="b">2. Our Recommendations<span class="lead"></span>03</li>
    <li class="l2">2.1. Our Approach<span class="lead"></span>05</li>
    <li class="l3">2.1.1. Budget and Timeframe<span class="lead"></span>07</li>
    <li>3. Appendix A: About Maple Creek<span class="lead"></span>10</li>
    <li class="l2">3.1. Appendix B: Selected Client List<span class="lead"></span>10</li>
    <li class="l3">3.1.1. Appendix C: Our Capabilities<span class="lead"></span>11</li>
    <li>Appendix D: Our Process<span class="lead"></span>12</li>
  </ul>
  <div class="footer"><div class="brand"><i></i>Oxa Cable Partners</div><div class="line"></div><div class="num">1</div></div>
</section>

<!-- Vision -->
<section class="page" style="left:597px;top:28px">
  <div class="dots"><i></i><i></i><i></i></div>
  <h2 class="title">Vision</h2>
  <div class="band">
    <div class="icon"><svg width="15" height="15" viewBox="0 0 20 20" fill="none" stroke="#fff" stroke-width="1.6"><circle cx="10" cy="10" r="8"/><circle cx="10" cy="10" r="4.5"/><circle cx="10" cy="10" r="1.2" fill="#fff"/><path d="M10 10 17 3"/></svg></div>
    <p class="txt">Ledgerly's mission is to help and support the self-employed and small business owners with their administrative tasks so they can focus on what matters – their business.</p>
  </div>
  <p class="body">Administrative tasks are cumbersome, time-consuming and often prevent small owners from focusing their time and energy on their business and their customers. They can also be extremely stressful and nerve-wracking for those attempting these tasks for the first time.</p>
  <p class="body">At Ledgerly, we envisage accounting for the self-employed and small business owners as being <span class="hl-red">automated and decentralized</span>.</p>
  <p class="body">Accounting can and should be done automatically. By connecting to all sources of accounting data such as bank accounts, payment systems, e-commerce websites, and invoicing systems, Ledgerly AI automatically completes these tasks, which would take hours to do manually. Bookings are created automatically and fully completed. Financial statements are available within a couple of clicks.</p>
  <p class="body">What may seem like a pipedream to the millions of self-employed who struggle with their admin, is already a reality. Now is the time to join Ledgerly on its mission to transform the world of bookkeeping through the power of AI.</p>
  <p class="sub">The Ledgerly model</p>
  <p class="body">Ledgerly is based on an innovative license model that uses Token-as-a-License (TaaL). The token represents lifelong software license for Ledgerly solutions. The pre-ICO token sales will enable Ledgerly to complete its development of Ledgerly AI to deliver fully automatic bookkeeping.</p>
  <p class="body">The pre-ICO token sale will also pave the way for a future Ledgerly ICO. Ledgerly will launch accounting on the blockchain and ensure your accounting data is comprehensive and private, but available everywhere within your preferred apps. Furthermore, a new range of business apps will connect to Ledgerly to provide you with leading edge business data access.</p>
  <p class="body">Ledgerly supports strong data ownership laws that truly protect individuals and ensure they have complete ownership of their data. Through decentralisation Ledgerly helps to ensure you always have full ownership of your data.</p>
  <p class="body">To find out more about the Ledgerly AI project, please register with your email at <a>www.ledgerly.example/ico</a> so we can notify you about our upcoming purchase periods.</p>
  <div class="footer"><div class="brand"><i></i>Oxa Cable Partners</div><div class="line"></div><div class="num">3</div></div>
</section>

<!-- Executive summary -->
<section class="page" style="left:28px;top:415px">
  <div class="dots"><i></i><i></i><i></i></div>
  <h2 class="title">Executive <span>Summary</span></h2>
  <p class="h-num">1&nbsp; Solution</p>
  <p class="it">AI automated accounting</p>
  <p class="body">Ledgerly builds automation in stages on top of its current system to reach full automation thanks to the Ledgerly AI. Ledgerly AI automates every manual task performed by the user. It starts by connecting to all sources of accounting data, such as bank account, credit card, webshop or document management systems. Based on these data, Ledgerly AI creates bookings and generates financial reports. Finally, Ledgerly AI features chat-like interface that allows users to communicate seamlessly with it, viewing it as a trusted advisor over time.</p>
  <p class="it">1.1&nbsp; Blockchain software license or Token-as-a-License (TaaL)</p>
  <p class="body">It is possible to create tokens on blockchain that represent software licenses, also known as Token-as-a-Licence (TaaL). Ledgerly creates TaaL by using the Kestrel official wallet which interacts with the Kestrel blockchain. Upon purchase of TaaL, the token holder is free to transfer or sell TaaL using secondary market that is built directly over the blockchain. Ledgerly checks the validity of a token against the blockchain ensuring that token holders have access to the software. TaaL makes distribution and securisation of software licenses easier for software developers. All in all, TaaL has a higher value as a normal software license.</p>
  <p class="h-num">2.&nbsp; Pre-ICO Token sale</p>
  <p class="body">To realize this innovative vision, Ledgerly is launching a pre-ICO in form of a token sale on Kestrel blockchain. 20,000,000 tokens are available to purchase for the price of CHF 0.10 each during a 30-day period to be announced. Tokens represent Ledgerly lifelong software licenses and by purchasing enough tokens, holders gain access to Ledgerly software. 15,000 tokens give access to Ledgerly invoicing or accounting. Future customers will still have the opportunity to buy directly yearly or monthly subscriptions to have access to Ledgerly.</p>
  <p class="sub">Future plans</p>
  <p class="body">A future ICO is planned between 18 and 24 months after the pre-ICO token sale. This offering will support the development of Ledgerly into a fully decentralized, privacy-focused ecosystem of applications. The new model will reward each participant so that a new world with zero administrative tasks becomes reality.</p>
  <div class="footer"><div class="brand"><i></i>Oxa Cable Partners</div><div class="line"></div><div class="num">2</div></div>
</section>

<!-- Headline two-column -->
<section class="page" style="left:316px;top:415px">
  <div class="dots"><i></i><i></i><i></i></div>
  <h2 class="title">Headline <span>Here</span></h2>
  <div class="cols">
    <div class="left">
      <div class="photo" role="img" aria-label="Photo of a hand drawing cloud network sketches with a marker" style="height:138px;margin-bottom:21px"></div>
      <div class="photo" role="img" aria-label="Photo of a businessman with a cloud computing sketch overlay" style="height:140px"></div>
    </div>
    <div class="right">
      <p class="quote">Ledgerly's mission is to help and support the self-employed and small business owners with their administrative tasks so they can focus on what matters – their business.</p>
      <p class="body">Administrative tasks are cumbersome, time-consuming and often prevent small owners from focusing their time and energy on their business and their customers. They can also be extremely stressful and nerve-wracking for those attempting these tasks for the first time.</p>
      <p class="body">At Ledgerly, we envisage accounting for the self-employed and small business owners as being <span class="hl">automated and decentralized</span>.</p>
      <p class="body">Accounting can and should be done automatically. By connecting to all sources of accounting data such as bank accounts, payment systems, e-commerce websites, and invoicing systems, Ledgerly AI automatically completes these tasks, which would take hours to do manually. Bookings are created automatically and fully completed. Financial statements are available within a couple of clicks, and after analysing your data, Ledgerly AI will offer you tips to improve your financial stability.</p>
      <p class="body">What may seem like a pipedream to the millions of self-employed who struggle with their admin.</p>
      <p class="sub">The Ledgerly model</p>
      <p class="body">Ledgerly is based on an innovative license model that uses Token-as-a-License (TaaL). The token represents lifelong software license for Ledgerly solutions. The pre-ICO token sales will enable Ledgerly to complete its development of Ledgerly AI to deliver fully automatic bookkeeping.</p>
    </div>
  </div>
  <div class="footer"><div class="brand"><i></i>Oxa Cable Partners</div><div class="line"></div><div class="num">6</div></div>
</section>

<!-- Our understanding -->
<section class="page" style="left:597px;top:415px">
  <div class="dots"><i></i><i></i><i></i></div>
  <h2 class="title">Our Understanding of <span>Your Needs</span></h2>
  <p class="quote">Ledgerly's mission is to help and support the self-employed and small business owners with their administrative tasks so they can focus on what matters – their business.</p>
  <p class="body">Administrative tasks are cumbersome, time-consuming and often prevent small owners from focusing their time and energy on their business and their customers. They can also be extremely stressful and nerve-wracking for those attempting these tasks for the first time.</p>
  <p class="body">At Ledgerly, we envisage accounting for the self-employed and small business owners as being <span class="hl">automated and decentralized</span>.</p>
  <p class="body">Accounting can and should be done automatically. By connecting to all sources of accounting data such as bank accounts, payment systems, e-commerce websites, and invoicing systems, Ledgerly AI automatically completes these tasks, which would take hours to do manually. Bookings are created automatically and fully completed. Financial statements are available within a couple of clicks.</p>
  <p class="body">What may seem like a pipedream to the millions of self-employed who struggle with</p>
  <p class="sub">The Ledgerly model</p>
  <p class="body">Ledgerly is based on an innovative license model that uses Token-as-a-License (TaaL). The token represents lifelong software license for Ledgerly solutions. The pre-ICO token sales will enable Ledgerly to complete its development of Ledgerly AI to deliver fully automatic bookkeeping.</p>
  <p class="body" style="margin-top:8px">Launch accounting on the blockchain and ensure your accounting data is comprehensive and private, but available everywhere within your preferred apps. It will empower you to manage your data as you see fit in a fully decentralized way. Furthermore, a new range of business apps will connect to Ledgerly to provide you with leading edge business data access.</p>
  <p class="body">Ledgerly supports strong data ownership laws that truly protect individuals and ensure they have complete ownership of their data. Through decentralisation Ledgerly helps to ensure you always have full ownership of your data.</p>
  <p class="body">To find out more about the Ledgerly AI project, please register with your email at <a>www.ledgerly.example</a> so we can notify you about our upcoming purchase periods.</p>
  <div class="footer"><div class="brand"><i></i>Oxa Cable Partners</div><div class="line"></div><div class="num">5</div></div>
</section>

<!-- Budget -->
<section class="page" style="left:28px;top:802px">
  <div class="dots"><i></i><i></i><i></i></div>
  <h2 class="title">Budget and <span>Timeframe</span></h2>
  <p class="sub" style="margin-top:0">Implementation Estimate</p>
  <p class="body">The bulk of the implementation costs will be defined by discovery. Based on similar CRM implementation projects, we feel expect that the CRM side will be somewhere between 200 and 300 hours, give or take. The wide swing in hours in phase one is related to the number of integration needs and our role in the integration project. Our focus in discovery will be to nail down these requirements and our role as it relates to what is needed to integrate the sites with the CRM.</p>
  <table>
    <tr><th style="width:58%">Task</th><th>Hours</th><th>Cost</th></tr>
    <tr><td>Discovery</td><td>40</td><td>$8,000</td></tr>
    <tr class="tot"><td colspan="3">Phase 1</td></tr>
    <tr><td>Discovery</td><td>20-40</td><td>$8,000</td></tr>
    <tr><td>Discovery</td><td>20-40</td><td>$8,000</td></tr>
    <tr><td>Discovery</td><td>20-40</td><td>$8,000</td></tr>
    <tr class="tot"><td>Total Phase 1</td><td>80-240</td><td>$16,800-40,000</td></tr>
    <tr class="tot"><td colspan="3">Phase 2</td></tr>
    <tr><td>Discovery</td><td>20-40</td><td>$8,000</td></tr>
    <tr class="tot"><td>Total Phase 2</td><td>80-240</td><td>$16,800-40,000</td></tr>
    <tr class="grand"><td>Total Estimated Implementation Cost</td><td>220-480</td><td>$44,000-96,000</td></tr>
  </table>
  <p class="sub" style="margin-top:0">Project Timeline</p>
  <p class="body">Based on the information we have at our disposal, the planned launch date does not seem a realistic goal to get both the work done needed to provide the foundation for the future CRM instance and the integration given the state of apparent flux of the requirements. That said, we feel it prudent to proceed with discovery before committing to or pushing that date. We are currently estimating that the first phase will take somewhere between 7 and 12 weeks (including discovery) to complete.</p>
  <table class="dark">
    <tr><th style="width:62%">Task</th><th>Weeks to Complete</th></tr>
    <tr><td>Discovery</td><td>1-2</td></tr>
    <tr><td>Phase 1</td><td>6-10</td></tr>
    <tr><td>Phase 2</td><td>8-12</td></tr>
    <tr class="grand"><td>Total Number of Weeks</td><td></td></tr>
  </table>
  <div class="footer"><div class="brand"><i></i>Oxa Cable Partners</div><div class="line"></div><div class="num">4</div></div>
</section>

<!-- Back cover -->
<section class="page" style="left:316px;top:802px">
  <div class="decor" role="img" aria-label="Soft pattern of pale green, blue and grey triangles" style="left:0;top:0;width:200px;height:300px;clip-path:polygon(30% 0,75% 0,100% 40%,70% 100%,25% 100%,0 45%)"></div>
  <div class="back-foot">
    <div class="brand"><i></i>Oxa Cable Partners</div>
    <div class="sep"></div>
    <div><span class="ic"></span>555-014-2290 Ext 120<br><span class="ic"></span>hello@oxacable.example<br><span class="ic"></span>www.oxacable.example</div>
    <div>210, 48 Harbour Lane Street<br>Northvale Province AB1 2CD</div>
  </div>
</section>

<!-- Headline full-width -->
<section class="page" style="left:597px;top:802px">
  <div class="dots"><i></i><i></i><i></i></div>
  <h2 class="title">Headline <span>Here</span></h2>
  <div class="photo" role="img" aria-label="Photo of a hand drawing cloud network sketches on a glass board" style="height:96px;margin-bottom:4px"></div>
  <p class="quote" style="color:var(--teal)">Ledgerly's mission is to help and support the self-employed and small business owners with</p>
  <p class="body">Administrative tasks are cumbersome, time-consuming and often prevent small owners from focusing their time and energy on their business and their customers. They can also be extremely stressful and nerve-wracking for those attempting these tasks for the first time.</p>
  <p class="body">At Ledgerly, we envisage accounting for the self-employed and small business owners as being <span class="hl">automated and decentralized</span>.</p>
  <p class="body">Accounting can and should be done automatically. By connecting to all sources of accounting data such as bank accounts, payment systems, e-commerce websites, and invoicing systems, Ledgerly AI automatically completes these tasks, which would take hours to do manually. Bookings are created automatically and fully completed. Financial statements are available within a couple of clicks.</p>
  <p class="body">What may seem like a pipedream to the millions of self-employed who struggle with their admin, is already a reality. Now is the time to join Ledgerly on its mission to transform the world of bookkeeping through the power of AI.</p>
  <p class="sub">The Ledgerly model</p>
  <p class="body">Ledgerly is based on an innovative license model that uses Token-as-a-License (TaaL). The token represents lifelong software license for Ledgerly solutions. The pre-ICO token sales will enable Ledgerly to complete its development of Ledgerly AI to deliver fully automatic bookkeeping.</p>
  <p class="body">With leading edge business data access to ensure you have the best available data at your fingertips.</p>
  <div class="footer"><div class="brand"><i></i>Oxa Cable Partners</div><div class="line"></div><div class="num">5</div></div>
</section>

</body>
</html>
```